Brochure for Varesh Law firm

We would like to have a brochure that describes the Firm ( about the firm) , the vision, the team , the practice areas. And the contact.
Varesh law firm has ranked as top Libyan law firms by Juris Ledger.
It will give a good picture if you look at www.varesh-example.ly

We can also provide more information if requested to share with designer.

```html
<!DOCTYPE html>
<html lang="en">
<head>
<meta charset="utf-8">
<title>Varesh Law firm – Brochure</title>
<link href="https://fonts.googleapis.com/css2?family=Oswald:wght@600;700&family=Open+Sans:wght@400;600;700&display=swap" rel="stylesheet">
<style>
:root{
  --bg:#dcdcdc;
  --navy:#2b303d;
  --navy-deep:#1f232d;
  --slate:#454b5a;
  --blue:#2443a8;
  --blue-light:#4a6fd0;
  --paper:#ffffff;
  --paper-grey:#eceded;
  --ink:#2a2d35;
  --muted:#c9ccd4;
  --photo-sky:#8fa6c4;
  --photo-stone:#b9a88c;
}
*{box-sizing:border-box;margin:0;padding:0}
html,body{width:1200px;height:2400px;overflow:hidden}
body{background:var(--bg);font-family:"Open Sans",Arial,sans-serif;color:var(--ink);position:relative}
.spread{position:absolute;left:30px;width:1140px;height:880px;display:flex;box-shadow:0 10px 30px rgba(0,0,0,.18)}
.spread--outside{top:200px}
.spread--inside{top:1240px}
.panel{position:relative;width:380px;height:880px;overflow:hidden}
.panel--dark{background:linear-gradient(160deg,var(--slate),var(--navy-deep));color:var(--paper)}
.panel--white{background:var(--paper)}
.panel--grey{background:linear-gradient(180deg,#f7f7f7,var(--paper-grey))}
.layer{position:absolute;left:0;top:0}
.heading{font-family:"Oswald",Arial,sans-serif;font-weight:700;text-transform:uppercase;letter-spacing:.5px}
.body-text{font-size:11.5px;line-height:1.65}
.wordmark{display:flex;align-items:center;gap:10px;font-family:"Open Sans",Arial,sans-serif;font-weight:600;letter-spacing:.5px}
.wordmark__square{width:14px;height:14px}

/* cover */
.cover__head{position:absolute;top:64px;left:20px;right:26px;text-align:right}
.cover__title{color:var(--blue);font-size:32px;line-height:1.05;white-space:nowrap}
.cover__tagline{margin-top:10px;font-size:12px;color:var(--ink);white-space:nowrap}
.cover__wordmark{position:absolute;left:150px;bottom:110px;color:var(--paper);font-size:34px}
.cover__wordmark .wordmark__square{background:var(--paper)}
.cover__url{position:absolute;right:28px;bottom:40px;font-size:12px;color:var(--muted);letter-spacing:1px}

/* back panel */
.back__wordmark{position:absolute;top:70px;left:0;right:0;justify-content:center;color:var(--ink);font-size:34px}
.back__wordmark .wordmark__square{background:var(--blue)}
.back__name{position:absolute;top:126px;width:100%;text-align:center;font-size:13px}
.back__badge{position:absolute;top:160px;left:160px;width:60px;height:60px;background:var(--navy-deep)}
.back__intro{position:absolute;top:250px;left:50px;right:50px;text-align:center;color:#555}
.back__contact-title{position:absolute;top:520px;width:100%;text-align:center;font-size:20px;color:var(--ink)}
.back__contact{position:absolute;top:560px;width:100%;text-align:center;font-size:13px;line-height:1.7;color:#444}
.contact-line{display:flex;justify-content:center;align-items:center;gap:6px}
.back__url{position:absolute;top:680px;width:100%;text-align:center;font-size:17px;font-weight:700;color:var(--blue)}

/* about */
.about__title{position:absolute;top:290px;left:36px;font-size:22px}
.about__text{position:absolute;top:332px;left:36px;right:32px;color:#d7dae2}
.about__text p{margin-bottom:10px}
.about__sub{font-family:"Oswald",Arial,sans-serif;font-weight:600;font-size:15px;color:var(--paper);margin:6px 0 4px}

/* vision */
.vision__title{position:absolute;top:40px;left:36px;font-size:22px}
.vision__text{position:absolute;top:84px;left:36px;right:32px;color:#d7dae2}
.vision__text p{margin-bottom:14px}

/* services */
.services__title{position:absolute;top:40px;width:100%;text-align:center;color:var(--blue);font-size:22px}
.services__grid{position:absolute;top:96px;left:24px;right:24px;display:grid;grid-template-columns:repeat(3,1fr);row-gap:26px;column-gap:8px}
.service{text-align:center}
.service__icon{width:46px;height:46px;border-radius:50%;background:var(--blue);margin:0 auto 6px;display:flex;align-items:center;justify-content:center}
.service__name{font-size:11.5px;font-weight:700;color:var(--blue);line-height:1.2}
.service__desc{font-size:9.5px;color:#666;line-height:1.35;margin-top:2px}
.services__ip{position:absolute;top:640px;left:0;right:0;height:240px;background:var(--paper);padding:0 32px}
.services__ip-title{font-family:"Oswald",Arial,sans-serif;font-weight:600;font-size:16px;color:var(--blue);margin-bottom:8px}
.services__ip p{color:#444}

/* team */
.team__wordmark{position:absolute;top:300px;left:34px;color:var(--paper);font-size:34px}
.team__wordmark .wordmark__square{background:var(--blue-light)}
.team__title{position:absolute;top:360px;left:34px;font-size:22px;color:var(--blue-light)}
.team__grid{position:absolute;top:404px;left:34px;right:34px;display:grid;grid-template-columns:repeat(4,1fr);gap:12px}
.portrait{height:88px;background:linear-gradient(180deg,#9a9ea6,#5d616a)}
</style>
</head>
<body>

<section class="spread spread--outside">

  <article class="panel panel--dark about">
    <svg class="layer" width="380" height="280" role="img" aria-label="Photo of a business team silhouetted against bright office windows">
      <defs><linearGradient id="teamPhoto" x1="0" y1="0" x2="0" y2="1"><stop offset="0" stop-color="#c9dcf2"/><stop offset="1" stop-color="#3b5c9a"/></linearGradient></defs>
      <polygon points="0,0 380,0 380,150 140,260 0,260" fill="url(#teamPhoto)"/>
    </svg>
    <svg class="layer" width="380" height="300">
      <polygon points="0,170 120,260 0,260" fill="var(--blue)"/>
    </svg>
    <h2 class="heading about__title">About the firm</h2>
    <div class="body-text about__text">
      <p>Varesh Law firm was founded in Tripoli to serve local and international clients with practical, reliable legal advice. Our lawyers combine deep knowledge of Libyan law with wide commercial experience, guiding companies, investors and public bodies through every stage of their work in Libya.</p>
      <h3 class="about__sub">Juris Ledger</h3>
      <p>Varesh Law firm has been ranked among the top Libyan law firms by Juris Ledger, a recognition of the trust our clients place in us and of the quality, speed and care we bring to each matter.</p>
      <p>We work in Arabic and English and keep close ties with firms abroad, so clients receive clear answers wherever their business leads them.</p>
    </div>
  </article>

  <article class="panel panel--grey back">
    <div class="wordmark back__wordmark"><span class="wordmark__square"></span>Varesh</div>
    <p class="back__name">Varesh Law Firm</p>
    <div class="back__badge" role="img" aria-label="Juris Ledger ranking badge"></div>
    <p class="body-text back__intro">At Varesh, we believe that lawyers are key agents of social change, with a responsibility to promote the rule of law and a stable business climate. We strive to become the firm of choice for clients seeking sound advice in Libya.</p>
    <h2 class="heading back__contact-title">Contact us</h2>
    <div class="back__contact">
      <p class="contact-line">
        <svg width="12" height="12" viewBox="0 0 24 24"><path d="M6 2l4 4-2 3c1 3 4 6 7 7l3-2 4 4-3 4C10 22 2 14 2 5z" fill="var(--blue)"/></svg>
        +218 21 555 0142</p>
      <p>12 Harbour Road, Meridian Tower</p>
      <p>P.O. Box 40512</p>
      <p>TRIPOLI Libya</p>
    </div>
    <p class="back__url">www.varesh-example.ly</p>
  </article>

  <article class="panel panel--white cover">
    <div class="cover__head">
      <h1 class="heading cover__title">Setting the<br>standard for Libya</h1>
      <p class="cover__tagline">Excellence is the hallmark of our legal solutions</p>
    </div>
    <svg class="layer" width="380" height="880">
      <defs><linearGradient id="coverDark" x1="0" y1="0" x2="1" y2="1"><stop offset="0" stop-color="#4a5060"/><stop offset="1" stop-color="#1c2029"/></linearGradient></defs>
      <polygon points="0,300 190,300 0,560" fill="var(--blue)"/>
      <polygon points="0,690 380,470 380,880 0,880" fill="url(#coverDark)"/>
    </svg>
    <svg class="layer" width="380" height="880" role="img" aria-label="Photo of modern office towers under a cloudy sky">
      <defs><linearGradient id="towerPhoto" x1="0" y1="0" x2="0" y2="1"><stop offset="0" stop-color="var(--photo-sky)"/><stop offset=".6" stop-color="var(--photo-stone)"/><stop offset="1" stop-color="#6f7a5e"/></linearGradient></defs>
      <polygon points="200,230 380,230 380,470 250,545 70,545" fill="url(#towerPhoto)"/>
    </svg>
    <svg class="layer" width="380" height="880" role="img" aria-label="Blue and white triangle mosaic decoration">
      <polygon points="250,545 380,470 380,600 300,640" fill="#5b79c8" opacity=".85"/>
    </svg>
    <div class="wordmark cover__wordmark"><span class="wordmark__square"></span>Varesh</div>
    <p class="cover__url">www.varesh-example.ly</p>
  </article>
</section>

<section class="spread spread--inside">

  <article class="panel panel--dark vision">
    <h2 class="heading vision__title">The vision</h2>
    <div class="body-text vision__text">
      <p>Libya has gone through many profound changes since 2011. Through each of them, our firm has stayed close to its clients, helping them adapt, protect their interests and plan with confidence. We see a future where sound legal practice supports growth, investment and lasting stability for the whole country.</p>
      <p>But in addition to this, we believe that lawyers are key agents of change. Our aim is to shape a modern legal market in Libya, and to be the firm clients turn to first when the stakes are high.</p>
    </div>
    <svg class="layer" width="380" height="880" role="img" aria-label="Photo of two business people shaking hands">
      <defs><linearGradient id="handshake" x1="0" y1="0" x2="1" y2="1"><stop offset="0" stop-color="#d9dde4"/><stop offset="1" stop-color="#7c8796"/></linearGradient></defs>
      <polygon points="0,690 130,620 380,620 380,880 0,880" fill="url(#handshake)"/>
    </svg>
    <svg class="layer" width="380" height="880">
      <polygon points="0,790 110,880 0,880" fill="var(--blue)"/>
    </svg>
  </article>

  <article class="panel panel--white services">
    <h2 class="heading services__title">Varesh law services</h2>
    <div class="services__grid">
      <div class="service"><div class="service__icon"><svg width="22" height="22" viewBox="0 0 24 24"><path d="M3 4h18v12H8l-5 4z" fill="none" stroke="#fff" stroke-width="2"/></svg></div><p class="service__name">Consultation</p><p class="service__desc">Practical advice on Libyan law</p></div>
      <div class="service"><div class="service__icon"><svg width="22" height="22" viewBox="0 0 24 24"><path d="M4 20h10M12 4l6 6M9 7l6 6M7 13l4 4" stroke="#fff" stroke-width="2" fill="none"/></svg></div><p class="service__name">Litigation</p><p class="service__desc">Representation before Libyan courts</p></div>
      <div class="service"><div class="service__icon"><svg width="22" height="22" viewBox="0 0 24 24"><path d="M12 3v18M5 7h14M5 7l-3 7h6zM19 7l-3 7h6z" stroke="#fff" stroke-width="2" fill="none"/></svg></div><p class="service__name">Arbitration</p><p class="service__desc">Local and international disputes</p></div>
      <div class="service"><div class="service__icon"><svg width="22" height="22" viewBox="0 0 24 24"><path d="M6 2h9l4 4v16H6zM9 10h7M9 14h7M9 18h5" stroke="#fff" stroke-width="2" fill="none"/></svg></div><p class="service__name">Contract Registration</p><p class="service__desc">Drafting and registering contracts</p></div>
      <div class="service"><div class="service__icon"><svg width="22" height="22" viewBox="0 0 24 24"><path d="M4 20V12M10 20V8M16 20V4M2 20h20" stroke="#fff" stroke-width="2" fill="none"/></svg></div><p class="service__name">Investment License</p><p class="service__desc">Licences for foreign investors</p></div>
      <div class="service"><div class="service__icon"><svg width="22" height="22" viewBox="0 0 24 24"><path d="M12 3l10 18H2zM12 10v5M12 17v2" stroke="#fff" stroke-width="2" fill="none"/></svg></div><p class="service__name">Legal Risk Assessment</p><p class="service__desc">Identifying risks before they arise</p></div>
      <div class="service"><div class="service__icon"><svg width="22" height="22" viewBox="0 0 24 24"><circle cx="10" cy="10" r="6" stroke="#fff" stroke-width="2" fill="none"/><path d="M15 15l6 6" stroke="#fff" stroke-width="2"/></svg></div><p class="service__name">Due Diligence</p><p class="service__desc">Thorough review of targets</p></div>
      <div class="service"><div class="service__icon"><svg width="22" height="22" viewBox="0 0 24 24"><path d="M12 2a6 6 0 0 1 4 10v3H8v-3a6 6 0 0 1 4-10zM9 19h6M10 22h4" stroke="#fff" stroke-width="2" fill="none"/></svg></div><p class="service__name">Intellectual Property</p><p class="service__desc">Protecting marks and patents</p></div>
    </div>
    <div class="services__ip">
      <h3 class="services__ip-title">Intellectual Property Services in Libya</h3>
      <p class="body-text">We offer our clients a full range of IP services, including trademark filing, patent and design protection, licensing and enforcement. Our team handles searches, oppositions and renewals, giving rights holders dependable protection across the Libyan market under current laws and regulations.</p>
    </div>
  </article>

  <article class="panel panel--dark team">
    <svg class="layer" width="380" height="300" role="img" aria-label="Photo of a lawyer reading documents at a desk">
      <defs><linearGradient id="deskPhoto" x1="0" y1="0" x2="1" y2="1"><stop offset="0" stop-color="#5c606a"/><stop offset="1" stop-color="#c8c3b8"/></linearGradient></defs>
      <polygon points="40,0 380,0 380,170 200,250 0,110" fill="url(#deskPhoto)"/>
    </svg>
    <svg class="layer" width="380" height="300">
      <polygon points="240,240 380,170 380,240" fill="var(--blue)"/>
    </svg>
    <div class="wordmark team__wordmark"><span class="wordmark__square"></span>Varesh</div>
    <h2 class="heading team__title">Our teem</h2>
    <div class="team__grid">
      <div class="portrait" role="img" aria-label="Team member portrait"></div>
      <div class="portrait" role="img" aria-label="Team member portrait"></div>
      <div class="portrait" role="img" aria-label="Team member portrait"></div>
      <div class="portrait" role="img" aria-label="Team member portrait"></div>
      <div class="portrait" role="img" aria-label="Team member portrait"></div>
      <div class="portrait" role="img" aria-label="Team member portrait"></div>
      <div class="portrait" role="img" aria-label="Team member portrait"></div>
      <div class="portrait" role="img" aria-label="Team member portrait"></div>
      <div class="portrait" role="img" aria-label="Team member portrait"></div>
      <div class="portrait" role="img" aria-label="Team member portrait"></div>
      <div class="portrait" role="img" aria-label="Team member portrait"></div>
      <div class="portrait" role="img" aria-label="Team member portrait"></div>
      <div class="portrait" role="img" aria-label="Team member portrait"></div>
      <div class="portrait" role="img" aria-label="Team member portrait"></div>
    </div>
  </article>
</section>

</body>
</html>
```